Business Flyer

I want an updated flyer that will have the same content as the one attached but in a different format. They flyers will be passed out to the community and local businesses.

```html
<!DOCTYPE html>
<html lang="en">
<head>
<meta charset="utf-8">
<title>Ripple Juice House – Community Flyer</title>
<link rel="stylesheet" href="https://fonts.googleapis.com/css2?family=Bebas+Neue&family=Lato:wght@400;700&display=swap">
<style>
  :root {
    --stage: #8f8f8f;
    --paper: #fdfbf8;
    --purple: #8a3a96;
    --orange: #f5a623;
    --ink: #3a3a3a;
    --white: #ffffff;
  }
  * { margin: 0; padding: 0; box-sizing: border-box; }
  html, body { width: 1200px; height: 1200px; overflow: hidden; }
  body {
    background: var(--stage);
    font-family: "Lato", sans-serif;
    position: relative;
  }
  .flyer {
    position: absolute;
    left: 204px; top: 40px;
    width: 792px; height: 1120px;
    background: radial-gradient(circle at 50% 38%, #ffffff 0%, var(--paper) 55%, #f6f1ea 100%);
    overflow: hidden;
    box-shadow: 0 6px 18px rgba(0,0,0,0.25);
  }
  .top-band { position: absolute; left: 0; top: 0; width: 792px; height: 40px; }
  .brand {
    position: absolute; top: 70px; left: 0; width: 100%;
    display: flex; justify-content: center; align-items: center; gap: 16px;
  }
  .brand-mark {
    width: 74px; height: 74px; border-radius: 50%;
    background: var(--purple);
  }
  .brand-name {
    font-family: "Bebas Neue", sans-serif;
    color: var(--purple);
    line-height: 0.9;
  }
  .brand-name .primary { display: block; font-size: 72px; }
  .brand-name .secondary { display: block; font-size: 22px; letter-spacing: 4px; }
  .hero-photo {
    position: absolute; left: 0; top: 228px;
    width: 792px; height: 350px;
  }
  .headline {
    position: absolute; left: 181px; top: 610px;
    display: flex; align-items: stretch; gap: 8px;
  }
  .headline-tag {
    background: var(--purple); color: var(--white);
    font-family: "Bebas Neue", sans-serif;
    font-size: 50px; line-height: 46px;
    writing-mode: vertical-rl; transform: rotate(180deg);
    text-align: center; padding: 4px 0;
    width: 48px;
  }
  .headline-lines { font-family: "Bebas Neue", sans-serif; line-height: 0.88; }
  .headline-lines .line-natural { display: block; font-size: 128px; color: var(--purple); }
  .headline-lines .line-cold { display: block; font-size: 104px; color: var(--orange); }
  .headline-lines .line-juices { display: block; font-size: 58px; color: var(--purple); letter-spacing: 0.5px; }
  .message-band { position: absolute; left: 0; top: 872px; width: 792px; height: 160px; }
  .message {
    position: absolute; left: 36px; top: 902px; width: 720px;
    color: var(--white); font-size: 17px; line-height: 21px; text-align: center;
  }
  .contact {
    position: absolute; left: 0; top: 1052px; width: 100%;
    display: flex; justify-content: center; align-items: center; gap: 18px;
    font-size: 18px; color: var(--ink);
  }
  .contact-item { display: flex; align-items: center; gap: 7px; }
  .contact-dot { width: 18px; height: 18px; border-radius: 50%; }
  .contact-dot.social-a { background: var(--orange); }
  .contact-dot.social-b { background: #3b5a9a; }
  .bottom-band { position: absolute; left: 0; bottom: 0; width: 792px; height: 8px; background: var(--paper); }
</style>
</head>
<body>
  <main class="flyer">
    <svg class="top-band" viewBox="0 0 792 40" aria-hidden="true">
      <path fill="#8a3a96" d="M0 0H792V30L760 32 720 28 680 33 630 29 590 34 540 30 500 33 450 28 400 32 350 29 300 34 250 30 200 33 150 28 100 32 50 29 0 34Z"/>
    </svg>

    <header class="brand">
      <span class="brand-mark"></span>
      <span class="brand-name">
        <span class="primary">Ripple</span>
        <span class="secondary">Juice House</span>
      </span>
    </header>

    <svg class="hero-photo" viewBox="0 0 792 350" role="img" aria-label="Photo of an orange juice glass and a berry smoothie with straw, sliced oranges, green leaves and juice splashes">
      <defs>
        <radialGradient id="heroTone" cx="50%" cy="55%" r="55%">
          <stop offset="0%" stop-color="#f7b733"/>
          <stop offset="45%" stop-color="#fbd67a"/>
          <stop offset="75%" stop-color="#e7c6ea"/>
          <stop offset="100%" stop-color="#fdfbf8" stop-opacity="0"/>
        </radialGradient>
      </defs>
      <rect width="792" height="350" fill="url(#heroTone)"/>
    </svg>

    <section class="headline">
      <span class="headline-tag">Smoothies</span>
      <h1 class="headline-lines">
        <span class="line-natural">Natural</span>
        <span class="line-cold">Cold Press</span>
        <span class="line-juices">Juices and Delicious</span>
      </h1>
    </section>

    <svg class="message-band" viewBox="0 0 792 160" aria-hidden="true">
      <path fill="#8a3a96" d="M0 8 40 4 90 9 140 3 200 8 260 2 320 7 380 3 440 9 500 4 560 8 620 2 680 7 740 3 792 6V150L750 154 700 149 650 156 600 151 540 157 480 150 420 155 360 149 300 156 240 151 180 157 120 150 60 155 0 150Z"/>
    </svg>
    <p class="message">Thank you for supporting your local business as we aim to provide you with a comfortable and inviting place coupled with great products that is conducive to changing people's lives and creating a positive community through our offerings of natural cold press juices and delicious smoothies!</p>

    <footer class="contact">
      <span class="contact-item"><span class="contact-dot social-a"></span>RIPPLE_JUICE_HOUSE</span>
      <span class="contact-item"><span class="contact-dot social-b"></span>Ripple Juice House</span>
      <span class="contact-item">
        <svg width="16" height="22" viewBox="0 0 16 22" aria-hidden="true">
          <path d="M8 1C4 1 1 4 1 8c0 5 7 13 7 13s7-8 7-13c0-4-3-7-7-7z" fill="none" stroke="#f5a623" stroke-width="2"/>
          <circle cx="8" cy="8" r="2.5" fill="#f5a623"/>
        </svg>
        4820 Orchard Lane Fairview, MD 20999
      </span>
    </footer>
  </main>
</body>
</html>
```